Construction Company Website Design

I need a Website Design for a Construction Company. I have attached logo and business card design files (a.i) to match styles and text for the website. I will need design for 3 pages:
1. A Home page
2. A secondary page (will be different information pages)
3. A contact page with submision form
Website to look professional and match the 'theme' across all pages, using main colours / reverse colours as per design files. Must be clear it is a construction related website without being over the top. Happy for the construction related details (whether that be images/outlines/backgrounds etc to be fairly subtle and not overbearing on the contect of the pages. It will be the content that will be most important, not the images within.

Content has not yet been fully completed but attached is a site map. Each page will need a space for the insertion of the relevant heading and associated content for that particular page. Example can be used as per attached map. If it is preferable to have content completed for this to be a more succesful project please advise and I will complete and submit.

Target Market(s)

Clients for potential construction projects. These could be a range of people. All would be very professional, well educated and put a substantial expection on the quality of website provided.

Industry/Entity Type

Construction

Number of Pages Required

3 page

Font styles to use
Serif
Sans Serif
Other font styles liked:
• fonts preferable as per design files provided unless designer beleives a different font would suit better

Requirements
Must have
• Colour scheme to match logo and business card files provided. Fonts that match as per provided files. Pages must be consistent with the theme carrying across all pages. All pages must have contact details at the bottom of the page.
• Contents of page 1 - 'Home page': multiple tab options / logo link
• Contents of page 2 - 'Secondary page': Top and side navigation / area for information and/or images.
• Contents of page - 'Contact us page': Top and side navigation / Submission form / area for logos such as linkdin, facebook etc.
Nice to have
• Would be good to have a or some generic construction related images - outlines / shadows / effects etc. These might be background images or outlines related to the relevant industry and are consistent across the pages. Could be outlines of buildings, images of men with hardhats etc etc. Good to see colour scheme as per design files used
Should not have
• No pictures of houses. Generally no photos. If any imagery of people must not show faces/details.

```html
<!DOCTYPE html>
<html lang="en">
<head>
<meta charset="utf-8">
<title>Northline Constructions</title>
<link href="https://fonts.googleapis.com/css2?family=Roboto:wght@400;500;700;900&family=Open+Sans:wght@400;600;700&display=swap" rel="stylesheet">
<style>
:root{
  --blue:#1b9ad7;
  --blue-dark:#14608f;
  --navy:#0b1838;
  --navy-deep:#071029;
  --red:#e0262b;
  --ink:#2b2f36;
  --muted:#7a808a;
  --line:#d9dde2;
  --pale:#f3f5f7;
  --white:#ffffff;
}
*{box-sizing:border-box;margin:0;padding:0}
html,body{width:1200px;height:3912px;overflow:hidden}
body{position:relative;font-family:"Open Sans",Arial,sans-serif;color:var(--ink);background:var(--white)}
.abs{position:absolute}
h2.section-title{position:absolute;left:0;width:1200px;text-align:center;font-family:"Roboto",Arial,sans-serif;font-weight:500;font-size:34px;color:var(--ink)}
h2.section-title::after{content:"";display:block;width:60px;height:3px;background:var(--blue);margin:12px auto 0}
.btn{position:absolute;background:var(--blue);color:var(--white);font:700 13px "Roboto",Arial,sans-serif;text-transform:uppercase;border-radius:16px;text-align:center;line-height:30px;height:30px;width:130px;letter-spacing:.5px}
.placeholder{position:absolute}

/* header */
.hero{left:0;top:0;width:1200px;height:540px;background:linear-gradient(135deg,#e8ecef 0%,#cfd6dc 45%,#eef1f3 100%)}
.topbar{left:0;top:0;width:1200px;height:100px;background:rgba(255,255,255,.55)}
.brand-group{left:72px;top:40px;height:34px;display:flex;align-items:center;gap:14px;white-space:nowrap}
.brand{display:flex;align-items:center;gap:10px;font:700 22px "Roboto",Arial,sans-serif;color:var(--navy)}
.brand-mark{width:14px;height:14px;background:var(--blue)}
.tagline{font:500 11px "Roboto",Arial,sans-serif;letter-spacing:1.5px;color:var(--navy);padding-left:14px;border-left:1px solid var(--navy)}
.nav{left:408px;top:40px;display:flex;font:500 12px "Roboto",Arial,sans-serif;text-transform:uppercase;white-space:nowrap}
.nav a{display:block;padding:0 18px;line-height:34px;color:var(--navy);text-decoration:none}
.nav a.active{background:var(--blue);color:var(--white)}
.hero-box{left:320px;top:218px;width:560px;height:206px;background:rgba(255,255,255,.8);text-align:center;padding-top:16px}
.hero-title{font:900 56px "Roboto",Arial,sans-serif;color:var(--blue);letter-spacing:3px;line-height:66px;white-space:nowrap}
.hero-sub{font-size:12px;font-weight:600;color:var(--navy)}
.hero-call{margin-top:18px;font:700 18px "Roboto",Arial,sans-serif;color:var(--red)}
.hero-phone{font:700 40px "Roboto",Arial,sans-serif;color:var(--navy);line-height:48px}

/* about */
.about-bg{left:0;top:560px;width:1200px;height:640px;background:var(--pale)}
.about-photo{left:616px;top:620px;width:584px;height:540px;background:linear-gradient(160deg,#8a6a3d,#c99a4c 40%,#3d4a5a)}
.about-card{left:72px;top:640px;width:620px;height:450px;background:var(--white);box-shadow:0 4px 18px rgba(0,0,0,.12);padding:42px 40px}
.about-card h2{font:700 38px "Roboto",Arial,sans-serif;color:var(--navy)}
.about-card h2::after{content:"";display:block;width:60px;height:3px;background:var(--blue);margin-top:8px}
.about-lead{margin-top:18px;font:700 18px "Roboto",Arial,sans-serif;color:var(--blue-dark);line-height:26px;text-transform:uppercase}
.about-card p{margin-top:14px;font-size:13px;line-height:21px;color:var(--muted)}
.about-card .btn{left:40px;top:380px}

/* services */
.service{width:300px;font-size:13px;line-height:20px;color:var(--muted)}
.service h3{font:700 15px "Roboto",Arial,sans-serif;color:var(--navy);margin-bottom:10px}
.icon{position:absolute;width:52px;height:52px;border-radius:50%;background:var(--blue)}
.device{left:496px;top:1318px;width:208px;height:420px;border-radius:28px;background:#1a1a1c}
.device-screen{left:510px;top:1372px;width:180px;height:316px;background:linear-gradient(180deg,#ffffff,#dfe6ec)}
.screen-name{left:510px;top:1392px;width:180px;text-align:center;font:700 28px "Roboto",Arial,sans-serif;color:var(--navy)}

/* projects */
.projects-bg{left:0;top:1800px;width:1200px;height:560px;background:linear-gradient(180deg,#eef1f4,#dde3e8)}
.projects-intro{left:260px;top:1936px;width:680px;text-align:center;font-size:13px;line-height:20px;color:var(--ink)}
.project{width:180px;text-align:center}
.project-ring{width:156px;height:156px;margin:0 auto;border-radius:50%;border:6px solid var(--blue);box-shadow:0 0 0 6px var(--white)}
.project p{margin-top:18px;font:700 13px "Roboto",Arial,sans-serif;color:var(--navy);line-height:19px}

/* news */
.news{width:336px}
.news-photo{width:336px;height:192px;position:relative}
.news-date{position:absolute;left:10px;bottom:-30px;width:54px;height:60px;background:var(--blue);color:var(--white);text-align:center;font:700 22px "Roboto",Arial,sans-serif;padding-top:8px;line-height:24px}
.news-date small{display:block;font-size:10px;font-weight:500}
.news h3{margin-top:44px;font:700 17px "Roboto",Arial,sans-serif;color:var(--navy);line-height:24px}
.news p{margin-top:12px;font-size:13px;line-height:20px;color:var(--muted)}
.dots{display:flex;gap:8px;margin-top:12px}
.dots span{width:12px;height:5px;border-radius:3px;background:var(--blue)}
.dots span+span{background:var(--line)}

/* contact */
.contact-bg{left:0;top:2980px;width:1200px;height:512px;background:linear-gradient(180deg,#ffffff,#eef1f4)}
.field{height:42px;border:1px solid var(--line);background:var(--white);font-size:13px;color:var(--muted);padding:12px 14px}
.field.area{height:172px}

/* footer */
.footer{left:0;top:3492px;width:1200px;height:368px;background:var(--navy)}
.footer-map{left:72px;top:3540px;width:440px;height:280px;background:linear-gradient(135deg,#e6e8e4,#cfd8cf)}
.footer-col h4{font:700 17px "Roboto",Arial,sans-serif;color:var(--white)}
.footer-col h4::after{content:"";display:block;width:40px;height:2px;background:var(--blue);margin-top:6px}
.addr{list-style:none;font-size:12px;color:#c6cbd6;line-height:20px}
.addr li{display:flex;align-items:center;gap:10px;margin-top:14px}
.addr svg{flex:none}
.social{display:flex;gap:12px}
.social span{width:34px;height:34px;background:var(--blue)}
.links{list-style:none;font:500 12px "Roboto",Arial,sans-serif;color:var(--white);text-transform:uppercase;width:200px}
.links li{border-bottom:1px solid rgba(255,255,255,.15);line-height:30px}
.copyright{left:0;top:3860px;width:1200px;height:52px;background:var(--navy-deep);color:#aab1c0;font-size:12px;text-align:center;line-height:52px}
</style>
</head>
<body>

<!-- Header & hero -->
<section class="hero abs" role="img" aria-label="Pale photo of construction blueprints with a hard hat"></section>
<div class="topbar abs"></div>
<div class="brand-group abs">
  <div class="brand"><span class="brand-mark"></span>NORTHLINE</div>
  <div class="tagline">COMPANY TAGLINE</div>
</div>
<nav class="nav abs">
  <a class="active">Home</a><a>About Us</a><a>Services ▾</a><a>Projects</a><a>Culture</a><a>News</a><a>Contact</a>
</nav>
<div class="hero-box abs">
  <div class="hero-title">CONSTRUCTIONS</div>
  <div class="hero-sub">Lorem Ipsum is simply dummy text of the printing and typesetting industry</div>
  <div class="hero-call">CALL US</div>
  <div class="hero-phone">0400 555 201</div>
</div>

<!-- About -->
<section class="about-bg abs"></section>
<div class="about-photo placeholder" role="img" aria-label="Photo of a builder from behind holding a yellow hard hat"></div>
<div class="about-card abs">
  <h2>About Us</h2>
  <div class="about-lead">Lorem Ipsum is simply dummy text of the printing and typesetting industry.</div>
  <p>Lorem Ipsum is simply dummy text of the printing and typesetting industry. Lorem Ipsum has been the industry's standard dummy text ever since the 1500s, when an unknown printer took a galley of type and scrambled it to make a type specimen book.</p>
  <p>Lorem Ipsum has been the industry's standard dummy text ever since the 1500s, when an unknown printer took.</p>
  <span class="btn">Read More</span>
</div>

<!-- Services -->
<h2 class="section-title" style="top:1236px">Services</h2>
<div class="device placeholder" role="img" aria-label="Smartphone showing a building sketch"></div>
<div class="device-screen abs"></div>
<div class="screen-name abs">NORTHLINE</div>

<div class="icon" style="left:384px;top:1386px"></div>
<div class="service abs" style="left:74px;top:1400px;text-align:right;width:290px"><h3>Building Maintenance</h3>Lorem Ipsum is simply dummy text of the printing and typesetting industry. Lorem Ipsum has been the industry's.</div>
<div class="icon" style="left:384px;top:1572px"></div>
<div class="service abs" style="left:74px;top:1586px;text-align:right;width:290px"><h3>Project Management</h3>Lorem Ipsum is simply dummy text of the printing and typesetting industry. Lorem Ipsum has been the industry's standard dummy text.</div>
<div class="icon" style="left:764px;top:1386px"></div>
<div class="service abs" style="left:832px;top:1400px"><h3>Commercial</h3>Lorem Ipsum is simply dummy text of the printing and typesetting industry. Lorem Ipsum has been the industry's.</div>
<div class="icon" style="left:764px;top:1572px"></div>
<div class="service abs" style="left:832px;top:1586px"><h3>Residential</h3>Lorem Ipsum is simply dummy text of the printing and typesetting industry. Lorem Ipsum has been the industry's standard dummy text.</div>

<!-- Projects -->
<section class="projects-bg abs" role="img" aria-label="Faded photo of a building site with cranes"></section>
<h2 class="section-title" style="top:1854px">Projects</h2>
<p class="projects-intro abs">Lorem Ipsum is simply dummy text of the printing and typesetting industry. Lorem Ipsum has been the industry's standard dummy text ever since the 1500s.</p>
<div class="project abs" style="left:106px;top:2000px"><div class="project-ring" role="img" aria-label="Project photo of a steel frame at dusk" style="background:linear-gradient(160deg,#3b2a3a,#a0563a)"></div><p>Lorem Ipsum is simply dummy</p></div>
<div class="project abs" style="left:372px;top:2000px"><div class="project-ring" role="img" aria-label="Project photo of a bridge under construction" style="background:linear-gradient(160deg,#5c7fa8,#c07a3a)"></div><p>Lorem Ipsum is simply dummy</p></div>
<div class="project abs" style="left:638px;top:2000px"><div class="project-ring" role="img" aria-label="Project photo of a crane against the sky" style="background:linear-gradient(160deg,#8fb8dc,#5a6c7c)"></div><p>Lorem Ipsum is simply dummy</p></div>
<div class="project abs" style="left:904px;top:2000px"><div class="project-ring" role="img" aria-label="Project photo of a timber roof frame" style="background:linear-gradient(160deg,#d9a25a,#6b4a2a)"></div><p>Lorem Ipsum is simply dummy</p></div>
<span class="btn" style="left:535px;top:2244px">View More</span>

<!-- News -->
<h2 class="section-title" style="top:2394px">News</h2>
<article class="news abs" style="left:72px;top:2468px">
  <div class="news-photo" role="img" aria-label="News photo of tower cranes on a site" style="background:linear-gradient(180deg,#9cc4e6,#b8a07a)"><div class="news-date">21<small>MAY</small></div></div>
  <h3>Lorem Ipsum is simply dummy text of the printing</h3>
  <p>Lorem Ipsum is simply dummy text of the printing and typesetting industry. Lorem Ipsum has been the industry's standard dummy text.</p>
  <div class="dots"><span></span><span></span></div>
</article>
<article class="news abs" style="left:432px;top:2468px">
  <div class="news-photo" role="img" aria-label="News photo of scaffolding and cranes" style="background:linear-gradient(180deg,#a9cde8,#8a8f7a)"><div class="news-date">21<small>MAY</small></div></div>
  <h3>Lorem Ipsum is simply dummy text of the printing</h3>
  <p>Lorem Ipsum is simply dummy text of the printing and typesetting industry. Lorem Ipsum has been the industry's standard dummy text.</p>
  <div class="dots"><span></span><span></span></div>
</article>
<article class="news abs" style="left:792px;top:2468px">
  <div class="news-photo" role="img" aria-label="News photo of a hard hat on building plans" style="background:linear-gradient(180deg,#e9c45a,#d8d2c4)"><div class="news-date">21<small>MAY</small></div></div>
  <h3>Lorem Ipsum is simply dummy text of the printing</h3>
  <p>Lorem Ipsum is simply dummy text of the printing and typesetting industry. Lorem Ipsum has been the industry's standard dummy text.</p>
  <div class="dots"><span></span><span></span></div>
</article>
<span class="btn" style="left:535px;top:2886px">View More</span>

<!-- Contact -->
<section class="contact-bg abs"></section>
<h2 class="section-title" style="top:3034px">Contact Us</h2>
<div class="field abs" style="left:88px;top:3116px;width:326px">Name</div>
<div class="field abs" style="left:438px;top:3116px;width:326px">Email</div>
<div class="field abs" style="left:788px;top:3116px;width:326px">Phone</div>
<div class="field area abs" style="left:88px;top:3186px;width:1026px">Message</div>
<span class="btn" style="left:530px;top:3404px;width:140px">Send Message</span>

<!-- Footer -->
<footer class="footer abs"></footer>
<div class="footer-map placeholder" role="img" aria-label="Street map showing the office location"></div>
<div class="footer-col abs" style="left:568px;top:3540px;width:340px">
  <h4>Our Address</h4>
  <ul class="addr">
    <li><svg width="14" height="14" viewBox="0 0 14 14"><path d="M3 1l2 3-1.5 1.5a8 8 0 0 0 5 5L10 9l3 2-1 2.5C6 13 1 8 .5 2z" fill="#1b9ad7"/></svg>0400 555 201</li>
    <li><svg width="14" height="14" viewBox="0 0 14 14"><path d="M7 0a5 5 0 0 1 5 5c0 4-5 9-5 9S2 9 2 5a5 5 0 0 1 5-5z" fill="#1b9ad7"/><circle cx="7" cy="5" r="2" fill="#0b1838"/></svg>12 Harbour Avenue, Westfield NSW 2000</li>
    <li><svg width="14" height="14" viewBox="0 0 14 14"><rect x="1" y="3" width="12" height="8" fill="#1b9ad7"/><path d="M1 3l6 5 6-5" stroke="#0b1838" fill="none"/></svg>hello@northlinebuild.example</li>
    <li><svg width="14" height="14" viewBox="0 0 14 14"><rect x="1" y="3" width="12" height="8" fill="#1b9ad7"/><path d="M1 3l6 5 6-5" stroke="#0b1838" fill="none"/></svg>www.northlinebuild.example</li>
  </ul>
  <h4 style="margin-top:22px">Follow Us</h4>
  <div class="social" style="margin-top:14px"><span></span><span></span><span></span><span></span><span></span></div>
</div>
<div class="footer-col abs" style="left:968px;top:3540px">
  <h4>Quick Links</h4>
  <ul class="links" style="margin-top:10px">
    <li>Home</li><li>About Us</li><li>Services</li><li>Projects</li><li>Culture</li><li>News</li><li>Contact</li>
  </ul>
</div>
<div class="copyright abs">© Northline Constructions 2024. All rights reserved. Terms and Conditions · Privacy Policy</div>

</body>
</html>
```